BUSINESS CARD - HALLORAN FIELD SERVICES

I would like to create a business card for my fertilizer spreading business. I would like to incorporate my existing logo and also a description of the services offered. The business card will be given to farmers so must be kept simple but effective. It will also be left in stores so much also be eye catching in order to stand out from other cards.

Target Market(s)

FARMERS

Requirements
Must have
• FRONT OF CARD = EXISTING LOGO + "CUSTOMISED SPREADING" below the logo

REAR Of CARD = SERVICES OFFERED AND CONTACT DETAILS

- Bulk fertilizer including Lime, Gypsum, Manure & Compost
- Granular fertilizer including Single Super, Urea, Gran-am, & Custom Blends
- Modern equipment - Autosteer & Variable Rate Capable
- Friendly & Reliable Service
- Contact Gus: 0471 592 318
Nice to have
• utilize same color scheme as existing logo

```html
<!DOCTYPE html>
<html lang="en">
<head>
<meta charset="utf-8">
<title>Halloran Field Services – Business Card</title>
<link href="https://fonts.googleapis.com/css2?family=Lato:wght@400;700&display=swap" rel="stylesheet">
<style>
  :root {
    --stage: #2a2a30;
    --card-dark: #232323;
    --card-light: #ffffff;
    --orange: #f08a12;
    --ink: #5a5a5e;
    --ink-soft: #7a7a7e;
    --white: #ffffff;
  }
  * { box-sizing: border-box; margin: 0; padding: 0; }
  html, body {
    width: 1200px; height: 800px; overflow: hidden;
    background: var(--stage);
    font-family: "Lato", Arial, sans-serif;
  }
  .stage { position: relative; width: 1200px; height: 800px; }

  .card {
    position: absolute;
    width: 540px; height: 309px;
    box-shadow: 0 14px 30px rgba(0,0,0,.45);
  }
  .card--services { left: 40px; top: 245px; background: var(--card-dark); color: var(--white); }
  .card--contact  { left: 620px; top: 245px; background: var(--card-light); color: var(--ink); }

  .brand { display: flex; flex-direction: column; align-items: flex-start; }
  .brand__row { display: flex; align-items: center; gap: 12px; }
  .brand__dot { width: 40px; height: 40px; border-radius: 50%; flex: none; }
  .brand__name { font-weight: 700; font-size: 22px; letter-spacing: -.2px; line-height: 1.1; }
  .brand__tagline {
    align-self: stretch;
    margin-top: 7px; padding-top: 5px;
    border-top: 1.5px solid var(--orange);
    color: var(--orange); font-weight: 700; font-size: 10px;
    letter-spacing: 2.4px; text-transform: uppercase; text-align: right;
  }

  .card--services .brand { position: absolute; left: 50%; top: 44px; transform: translateX(-50%); }
  .card--services .brand__dot { background: var(--white); }
  .card--services .brand__name { color: var(--white); }

  .services {
    position: absolute; left: 20px; right: 20px; top: 150px;
    list-style: none; text-align: center;
    font-size: 11.5px; line-height: 1.75; font-weight: 400;
  }

  .card--contact .brand { position: absolute; right: 30px; top: 34px; }
  .card--contact .brand__dot { background: var(--ink); }
  .card--contact .brand__name { color: var(--ink); }

  .divider {
    position: absolute; left: 220px; right: 30px; top: 150px;
    height: 1px; background: var(--ink-soft);
  }

  .person { position: absolute; left: 34px; top: 128px; }
  .person__name { color: var(--orange); font-weight: 700; font-size: 24px; line-height: 1.1; }
  .person__role { color: var(--ink); font-size: 14px; margin-top: 3px; }

  .contact-list {
    position: absolute; left: 34px; top: 200px; list-style: none;
    font-size: 12.5px; line-height: 1.6; color: var(--ink);
  }
  .contact-list li { display: flex; align-items: center; gap: 9px; }
  .contact-list svg { width: 11px; height: 11px; fill: var(--orange); flex: none; }

  .address {
    position: absolute; right: 30px; top: 176px;
    font-size: 13px; line-height: 1.45; color: var(--ink); font-style: normal;
  }
</style>
</head>
<body>
<main class="stage">

  <section class="card card--services" aria-label="Card front: services">
    <div class="brand">
      <div class="brand__row">
        <span class="brand__dot"></span>
        <span class="brand__name">Halloran Field Services</span>
      </div>
      <span class="brand__tagline">Customised Spreading</span>
    </div>
    <ul class="services">
      <li>Modern equipment – Autosteer &amp; Variable Rate Capable</li>
      <li>Friendly &amp; Reliable Service</li>
      <li>Bulk fertilizer including Lime, Gypsum, Manure &amp; Compost</li>
      <li>Granular fertilizer including Single Super, Urea, Gran-am, &amp; Custom Blends</li>
    </ul>
  </section>

  <section class="card card--contact" aria-label="Card back: contact details">
    <div class="brand">
      <div class="brand__row">
        <span class="brand__dot"></span>
        <span class="brand__name">Halloran Field Services</span>
      </div>
      <span class="brand__tagline">Customised Spreading</span>
    </div>

    <div class="divider"></div>

    <div class="person">
      <p class="person__name">Gus Whitcombe</p>
      <p class="person__role">Co-founder</p>
    </div>

    <ul class="contact-list">
      <li>
        <svg viewBox="0 0 24 24" aria-hidden="true"><path d="M6.6 10.8a15.1 15.1 0 0 0 6.6 6.6l2.2-2.2a1 1 0 0 1 1-.25 11.4 11.4 0 0 0 3.6.57 1 1 0 0 1 1 1V20a1 1 0 0 1-1 1A17 17 0 0 1 3 4a1 1 0 0 1 1-1h3.5a1 1 0 0 1 1 1c0 1.25.2 2.45.57 3.6a1 1 0 0 1-.25 1z"/></svg>
        0471 592 318
      </li>
      <li>
        <svg viewBox="0 0 24 24" aria-hidden="true"><path d="M7 1h10a2 2 0 0 1 2 2v18a2 2 0 0 1-2 2H7a2 2 0 0 1-2-2V3a2 2 0 0 1 2-2zm0 3v14h10V4zm5 15.5a1.2 1.2 0 1 0 0 2.4 1.2 1.2 0 0 0 0-2.4z"/></svg>
        0471 592 319
      </li>
      <li>
        <svg viewBox="0 0 24 24" aria-hidden="true"><path d="M2 5h20v14H2zm2 2v.5l8 5 8-5V7zm0 2.8V17h16V9.8l-8 5z"/></svg>
        hello@halloranfield.com
      </li>
      <li>
        <svg viewBox="0 0 24 24" aria-hidden="true"><path d="M12 2a10 10 0 1 0 0 20 10 10 0 0 0 0-20zm0 2c.9 0 2.2 1.8 2.8 5H9.2C9.8 5.8 11.1 4 12 4zM4.3 11h4.6a20 20 0 0 0 0 2H4.3a8 8 0 0 1 0-2zm6.6 0h2.2a18 18 0 0 1 0 2h-2.2a18 18 0 0 1 0-2zm4.2 0h4.6a8 8 0 0 1 0 2h-4.6a20 20 0 0 0 0-2zM9.2 15h5.6c-.6 3.2-1.9 5-2.8 5s-2.2-1.8-2.8-5z"/></svg>
        www.halloranfield.com
      </li>
    </ul>

    <address class="address">
      2140 Riverside, Mill<br>Lane 8-12.
    </address>
  </section>

</main>
</body>
</html>
```